Banner Ad for Resume Services Website

The add is for this web site: www.BrightCareerPages.net

The site offers 4 different services:

- Resume Writing (by a Certified Professional Resume Writer)
- Resume Posting (posts your resume to 85 job sites)
- Resume Distribution (sends your resume to hundreds of recruiters)
- Resume Online website (created an online resume with a domain name to your name)

Colors to be used are Blue, Yellow, etc... please check the website for inspiration.

Check the web site to learn more.

Target Market(s)

Unemployed, Professionals who want to switch jobs, etc..

Industry/Entity Type

Requirements
Must have
• We definitely one this to be included on the banner:

"Free Resume Samples"

in order to attract clicks.
Nice to have
• Some of the words we suggest to include on the banner are:

"How Good is Your Resume? Ask a Professional !"

Should not have
• No animation !

Do not place the LOGO on the banner as our LOGO might change in the near future. If you already submitted a banner with the LOGO on it, you can replace it with any other graphic that has a Resume/Jobs/BusinessStaff related theme.

```html
<!DOCTYPE html>
<html lang="en">
<head>
<meta charset="utf-8">
<title>Resume Services Banner</title>
<link rel="stylesheet" href="https://fonts.googleapis.com/css2?family=Titillium+Web:wght@300;400&display=swap">
<style>
  :root {
    --canvas-top: #ffffff;
    --canvas-bottom: #efefef;
    --banner-top: #1e6dcc;
    --banner-mid: #135ab4;
    --banner-bottom: #0a3c86;
    --banner-edge: #14284a;
    --headline: #ffffff;
    --offer: #f07a1e;
    --icon: #ffffff;
  }
  * { margin: 0; padding: 0; box-sizing: border-box; }
  html, body {
    width: 1200px;
    height: 407px;
    overflow: hidden;
  }
  body {
    position: relative;
    background: linear-gradient(180deg, var(--canvas-top) 0%, #fafafa 45%, var(--canvas-bottom) 100%);
    font-family: "Titillium Web", sans-serif;
  }
  .banner {
    position: absolute;
    left: 181px;
    top: 140px;
    width: 874px;
    height: 108px;
    border: 1px solid var(--banner-edge);
    background: linear-gradient(180deg, var(--banner-top) 0%, var(--banner-mid) 45%, var(--banner-bottom) 100%);
  }
  .banner__icon {
    position: absolute;
    left: 0;
    top: 0;
    width: 120px;
    height: 106px;
  }
  .banner__copy {
    position: absolute;
    left: 118px;
    width: 680px;
    top: 18px;
    text-align: center;
    line-height: 1;
  }
  .banner__headline {
    display: block;
    color: var(--headline);
    font-weight: 400;
    font-size: 31px;
    letter-spacing: -0.3px;
  }
  .banner__offer {
    display: block;
    margin-top: 8px;
    color: var(--offer);
    font-weight: 300;
    font-size: 28px;
    letter-spacing: -0.2px;
  }
  .reflection {
    position: absolute;
    left: 181px;
    top: 248px;
    width: 874px;
    height: 108px;
    overflow: hidden;
    -webkit-mask-image: linear-gradient(180deg, rgba(0,0,0,0.35) 0%, rgba(0,0,0,0.12) 35%, rgba(0,0,0,0) 60%);
            mask-image: linear-gradient(180deg, rgba(0,0,0,0.35) 0%, rgba(0,0,0,0.12) 35%, rgba(0,0,0,0) 60%);
  }
  .reflection .banner {
    left: 0;
    top: 0;
    transform: scaleY(-1);
  }
</style>
</head>
<body>
  <a class="banner" href="#" aria-label="How Good is Your Resume? Ask a Professional! Free Resume Samples">
    <svg class="banner__icon" viewBox="0 0 120 106" aria-hidden="true">
      <circle cx="73" cy="36" r="27" fill="none" stroke="var(--icon)" stroke-width="6"/>
      <line x1="54" y1="56" x2="22" y2="94" stroke="var(--icon)" stroke-width="11" stroke-linecap="round"/>
    </svg>
    <div class="banner__copy">
      <span class="banner__headline">How Good is Your Resume? Ask a Professional !</span>
      <span class="banner__offer">Free Resume Samples</span>
    </div>
  </a>

  <div class="reflection" aria-hidden="true">
    <div class="banner">
      <svg class="banner__icon" viewBox="0 0 120 106">
        <circle cx="73" cy="36" r="27" fill="none" stroke="var(--icon)" stroke-width="6"/>
        <line x1="54" y1="56" x2="22" y2="94" stroke="var(--icon)" stroke-width="11" stroke-linecap="round"/>
      </svg>
      <div class="banner__copy">
        <span class="banner__headline">How Good is Your Resume? Ask a Professional !</span>
        <span class="banner__offer">Free Resume Samples</span>
      </div>
    </div>
  </div>
</body>
</html>
```